Bright Harbour Learning business card design

Needing a business card design using an existing logo. Double sided card and we will be printing using rounded corners. Can also use metallics if appropriate. The design needs to be professional and modern.

Target Market(s)

Professional organisations

Industry/Entity Type

Business

Contact Information for Business Card

busines name, person name, email, website, phone, address,

Colors

Designer to choose colors to be used in the design.

Requirements
Must have
• Use existing 'Bright Harbour Learning' logo Using uploaded logo design. Simple and modern design. Black,white,silver,greys as the dominant colouring. Can introduce another single colour. Must also include a small version of the attached 'KLV' logo on the card (white and black versions uploaded also)
Nice to have
• Something modern
Should not have
• Additional images

```html
<!DOCTYPE html>
<html lang="en">
<head>
<meta charset="utf-8">
<title>Bright Harbour Learning – Business Card</title>
<link rel="stylesheet" href="https://fonts.googleapis.com/css2?family=Libre+Baskerville&family=Open+Sans:wght@600&display=swap">
<style>
  :root {
    --page-bg: #e6e3df;
    --card-light: #f3f2f0;
    --card-silver: #d9d7d4;
    --ink: #1d1b1a;
    --ink-soft: #4a4644;
    --band-grey: #5c5856;
    --band-dark: #1a1817;
    --band-text: #d8d3cf;
    --band-muted: #a39c97;
    --badge: #2a2827;
  }
  * { margin: 0; padding: 0; box-sizing: border-box; }
  html, body { width: 1200px; height: 970px; overflow: hidden; background: var(--page-bg); }
  .card {
    position: absolute; left: 100px; top: 200px; width: 1000px; height: 569px;
    border-radius: 8px; overflow: hidden;
    background: linear-gradient(160deg, var(--card-light) 0%, var(--card-silver) 100%);
    box-shadow: 0 12px 40px rgba(0,0,0,.18);
    font-family: "Libre Baskerville", Georgia, serif;
    color: var(--ink);
  }
  .card-shapes { position: absolute; inset: 0; }
  .brand { position: absolute; left: 60px; top: 80px; display: flex; align-items: center; gap: 22px; }
  .brand-dot { width: 72px; height: 72px; border-radius: 50%; background: var(--ink); flex: none; }
  .brand-name { font-size: 38px; line-height: 44px; text-transform: uppercase; letter-spacing: 1px; text-align: right; color: var(--ink); }
  .brand-tagline { position: absolute; left: 94px; top: 250px; font-size: 14px; color: var(--ink); }
  .person { position: absolute; right: 54px; top: 76px; text-align: right; }
  .person-name { font-size: 30px; text-transform: uppercase; }
  .person-role { font-size: 22px; color: var(--ink-soft); margin-top: 2px; }
  .member { position: absolute; left: 730px; top: 312px; display: flex; align-items: center; gap: 14px; }
  .member-badge { width: 76px; height: 62px; border-radius: 50%; background: var(--badge); }
  .member-text { border-left: 1px solid var(--ink); padding-left: 12px; font-family: "Open Sans", Arial, sans-serif; font-weight: 600; font-size: 13px; line-height: 16px; }
  .contact { position: absolute; left: 50px; top: 352px; color: var(--band-text); font-size: 23px; line-height: 32px; }
  .contact-row { display: flex; align-items: center; gap: 14px; }
  .contact-icon { width: 26px; height: 26px; }
  .website { position: absolute; left: 50px; top: 522px; color: var(--band-muted); font-size: 21px; }
  .social { position: absolute; right: 54px; top: 494px; display: flex; gap: 22px; }
  .social-square { width: 42px; height: 42px; border-radius: 3px; background: var(--card-silver); }
</style>
</head>
<body>
<div class="card">
  <svg class="card-shapes" viewBox="0 0 1000 569" width="1000" height="569" aria-hidden="true">
    <polygon points="0,302 585,302 645,235 692,235 576,336 700,449 1000,449 1000,569 0,569" fill="var(--band-grey)"/>
    <polygon points="0,338 600,338 668,262 692,262 590,350 712,472 1000,472 1000,569 0,569" fill="var(--band-dark)"/>
    <polygon points="0,500 0,569 560,569 520,500" fill="#4a4644" opacity=".55"/>
  </svg>

  <div class="brand">
    <span class="brand-dot"></span>
    <div class="brand-name">Bright<br>Harbour<br>Learning</div>
  </div>
  <div class="brand-tagline">Evidence-Based Training &amp; Development</div>

  <div class="person">
    <div class="person-name">Daniel Reeve</div>
    <div class="person-role">Managing Partner</div>
  </div>

  <div class="member">
    <span class="member-badge"></span>
    <div class="member-text">Member<br>Kingsford<br>Learning<br>Venture MKLV</div>
  </div>

  <div class="contact">
    <div>PO BOX 456 Harbour Lane</div>
    <div>14 Quay Street, Sydney</div>
    <div class="contact-row">
      <svg class="contact-icon" viewBox="0 0 26 26" aria-hidden="true"><rect width="26" height="26" rx="3" fill="#3a3634"/><path d="M8 7c1-1 2 0 3 2s0 2-1 3c1 2 2 3 4 4 1-1 1-2 3-1s3 2 2 3c-2 3-6 1-9-2S5 9 8 7z" fill="#8c8580"/></svg>
      <span>(02) 4815 1623</span>
    </div>
    <div class="contact-row">
      <svg class="contact-icon" viewBox="0 0 26 26" aria-hidden="true"><rect width="26" height="26" rx="3" fill="#3a3634"/><rect x="5" y="8" width="16" height="11" fill="none" stroke="#8c8580" stroke-width="1.6"/><path d="M5 8l8 6 8-6" fill="none" stroke="#8c8580" stroke-width="1.6"/></svg>
      <span>hello@brightharbour.com</span>
    </div>
  </div>

  <div class="website">www.brightharbour.com</div>

  <div class="social">
    <span class="social-square"></span>
    <span class="social-square"></span>
  </div>
</div>
</body>
</html>
```